B2B modern industry lubrication label

We are a chemical company that needs a new, very modern outstanding lubrication packaging label. The logo attached can be changed in color. The name of the product is R83. Attached also the text you can use, please disregard the current layout of the text, you can make it any layout you want. Be free in font type, colors and other design aspects.
Dimensions: 21 x 14,8 cm
industry, companies with machinery
Industrial

```html
<!DOCTYPE html>
<html lang="en">
<head>
<meta charset="utf-8">
<title>HALDEN Lubricant – 5W-30 R83 label</title>
<link rel="stylesheet" href="https://fonts.googleapis.com/css2?family=Ubuntu:wght@300;400;500;700&display=swap">
<style>
  :root {
    --page-bg: #b4bdd0;
    --label-top: #4a3a1c;
    --label-mid: #2f2409;
    --label-bottom: #3a2a08;
    --band: #050505;
    --brand-red: #d6291c;
    --cream: #f3cfa6;
    --tan: #e7b98c;
    --white: #f4f4f4;
  }
  html, body {
    margin: 0;
    padding: 0;
    width: 1200px;
    height: 900px;
    overflow: hidden;
    background: var(--page-bg);
    font-family: "Ubuntu", sans-serif;
  }
  .label {
    position: absolute;
    left: 360px;
    top: 41px;
    width: 480px;
    height: 818px;
  }
  .label-shape {
    position: absolute;
    inset: 0;
    width: 480px;
    height: 818px;
  }
  .brand {
    position: absolute;
    left: 0;
    width: 100%;
    text-align: center;
    padding-left: 40px;
    box-sizing: border-box;
  }
  .brand-name {
    top: 132px;
    font-size: 82px;
    font-weight: 700;
    line-height: 1;
    color: var(--brand-red);
    letter-spacing: -1px;
  }
  .brand-tagline {
    top: 232px;
    font-size: 24px;
    font-weight: 400;
    letter-spacing: 14px;
    color: var(--white);
  }
  .grade {
    position: absolute;
    top: 348px;
    left: 0;
    width: 100%;
    height: 126px;
    display: flex;
    align-items: center;
    justify-content: center;
    padding-left: 20px;
    box-sizing: border-box;
    font-size: 64px;
    font-weight: 400;
    letter-spacing: 2px;
    color: var(--cream);
  }
  .product-code {
    position: absolute;
    top: 488px;
    left: 0;
    width: 100%;
    text-align: center;
    padding-left: 20px;
    box-sizing: border-box;
    font-size: 40px;
    font-weight: 300;
    color: var(--cream);
  }
  .line-name {
    position: absolute;
    left: 34px;
    top: 666px;
    font-size: 28px;
    font-weight: 400;
    color: var(--tan);
    margin: 0;
  }
  .features {
    position: absolute;
    left: 28px;
    top: 708px;
    margin: 0;
    padding: 0;
    list-style: none;
    font-size: 14.5px;
    line-height: 20px;
    font-weight: 500;
    color: var(--tan);
  }
  .volume {
    position: absolute;
    right: 26px;
    top: 750px;
    font-size: 24px;
    font-weight: 400;
    color: var(--cream);
  }
</style>
</head>
<body>
  <div class="label">
    <svg class="label-shape" viewBox="0 0 480 818" aria-hidden="true">
      <defs>
        <linearGradient id="label-fill" x1="0" y1="0" x2="0" y2="1">
          <stop offset="0" stop-color="var(--label-top)"/>
          <stop offset="0.45" stop-color="var(--label-mid)"/>
          <stop offset="1" stop-color="var(--label-bottom)"/>
        </linearGradient>
        <radialGradient id="label-glow" cx="0.55" cy="0.25" r="0.45">
          <stop offset="0" stop-color="#7a5a26" stop-opacity="0.55"/>
          <stop offset="1" stop-color="#7a5a26" stop-opacity="0"/>
        </radialGradient>
        <clipPath id="label-clip">
          <path d="M124 0 H380 Q460 0 480 150 V800 Q480 818 462 818 H18 Q0 818 0 800 V140 Q0 30 124 0 Z"/>
        </clipPath>
      </defs>
      <g clip-path="url(#label-clip)">
        <rect width="480" height="818" fill="url(#label-fill)"/>
        <rect width="480" height="818" fill="url(#label-glow)"/>
        <rect y="348" width="480" height="126" fill="var(--band)"/>
      </g>
    </svg>

    <div class="brand brand-name">HALDEN</div>
    <div class="brand brand-tagline">LUBRICANT</div>

    <div class="grade">5W-30</div>
    <div class="product-code">R83</div>

    <h2 class="line-name">Omni- Drive</h2>
    <ul class="features">
      <li>drives off the eventually present moisture</li>
      <li>handle temperatures until 370°C.</li>
      <li>extremely thin and smooth layer of grease</li>
      <li>helps prevent “pitting wear”.</li>
    </ul>
    <div class="volume">50ml.</div>
  </div>
</body>
</html>
```